Brightvane Printers 1/4 page mag ad

I need an advert for 1/4 page Sydney law society magazine
Size 122mm tall x 89mm accross or 250mm tall x 42mm accress. full colour
We give free Copiers (mfps) to lawyers and charge per page.
The copiers we supply can be seen at www.brightvaneprinters.com.au. The Q Module 738K is the most common one we put out to solicitors
The copycost plans are seen on the frontpage along with the logo and machine photos
I would like to emphasise 'No lock in contracts'
We supply to Sydney and inner suburbs
I would like to target lawyers who are thinking of leaving their present employers and starting their own practice.
"Free to Members of the Counsel Guild of NSW"
email is info@brightvaneprinters.com.au
Phone is 1800 27 91 58
Cheers
Rob
Updates

Project Deadline Extended
Reason: The setup is portrait not landscape. a few wording changes.

Target Market(s)

I would like to target lawyers who are thinking of leaving their present employers and starting their own practice

Requirements
Must have
• Sydney and inner suburbs
No Lock-in Contracts
Free Copiers to Members of the Counsel Guild of NSW
Logo
Nice to have
• 10000 Secure Customer Codes that count copies, prints, scans & faxes for acurate billing

```html
<!DOCTYPE html>
<html lang="en">
<head>
<meta charset="utf-8">
<title>Brightvane Printers – Quarter Page Advert</title>
<link rel="stylesheet" href="https://fonts.googleapis.com/css2?family=Source+Sans+3:ital,wght@0,600;0,700;1,600;1,700&family=PT+Sans+Narrow:wght@700&display=swap">
<style>
  :root {
    --brand-red: #d0232c;
    --panel-white: #ffffff;
    --ink: #231f20;
    --burst: #231f20;
    --machine-light: #eceded;
    --machine-mid: #c9ccd0;
    --machine-dark: #7d8691;
  }
  * { margin: 0; padding: 0; box-sizing: border-box; }
  html, body { width: 875px; height: 1200px; overflow: hidden; background: var(--brand-red); }
  .advert {
    position: relative;
    width: 875px;
    height: 1200px;
    background: var(--brand-red);
    font-family: "Source Sans 3", "Myriad Pro", sans-serif;
    overflow: hidden;
  }
  .headline {
    position: absolute;
    left: 0; right: 0; top: 17px;
    text-align: center;
    color: var(--panel-white);
    font-weight: 700;
    font-size: 101px;
    line-height: 101px;
    letter-spacing: -0.5px;
    white-space: nowrap;
  }
  .member-line {
    position: absolute;
    left: 0; right: 0; top: 243px;
    text-align: center;
    color: var(--panel-white);
    font-weight: 700;
    font-size: 46px;
    line-height: 50px;
    white-space: nowrap;
  }
  .content-panel {
    position: absolute;
    left: 8px; right: 9px;
    top: 406px; height: 714px;
    background: var(--panel-white);
  }
  .machine-photo {
    position: absolute;
    left: 305px; top: 337px;
    width: 561px; height: 525px;
    background: linear-gradient(160deg, var(--machine-light) 0%, var(--machine-mid) 60%, var(--machine-dark) 100%);
    border-radius: 6px;
  }
  .feature-burst {
    position: absolute;
    left: 17px; top: 341px;
    width: 252px; height: 252px;
  }
  .feature-burst svg { position: absolute; inset: 0; width: 100%; height: 100%; }
  .feature-burst p {
    position: absolute;
    inset: 0;
    display: flex; align-items: center; justify-content: center;
    text-align: center;
    color: var(--panel-white);
    font-style: italic;
    font-weight: 700;
    font-size: 33px;
    line-height: 37.5px;
    white-space: nowrap;
  }
  .billing-note {
    position: absolute;
    left: 32px; top: 599px;
    color: var(--ink);
    font-family: "PT Sans Narrow", "Arial Narrow", sans-serif;
    font-weight: 700;
    font-size: 24px;
    line-height: 41.6px;
    white-space: nowrap;
  }
  .contract-line {
    position: absolute;
    left: 24px; top: 855px;
    color: var(--ink);
    font-weight: 700;
    font-size: 92px;
    line-height: 96px;
    letter-spacing: -0.5px;
    white-space: nowrap;
  }
  .brand-name {
    position: absolute;
    left: 23px; top: 966px;
    color: var(--brand-red);
    font-weight: 700;
    font-size: 62px;
    line-height: 60px;
    white-space: nowrap;
  }
  .service-area {
    position: absolute;
    left: 445px; top: 1004px;
    color: var(--ink);
    font-style: italic;
    font-weight: 600;
    font-size: 50px;
    line-height: 48px;
    white-space: nowrap;
  }
  .contact-bar {
    position: absolute;
    left: 0; right: 0; top: 1140px;
    text-align: center;
    color: var(--panel-white);
    font-weight: 700;
    font-size: 38px;
    line-height: 46px;
    white-space: nowrap;
  }
  .contact-bar .divider { margin: 0 12px; }
</style>
</head>
<body>
<main class="advert">
  <h1 class="headline">FREE Photocopiers<br>and Printers</h1>
  <p class="member-line">for members of the Counsel Guild of NSW</p>

  <section class="content-panel"></section>

  <div class="machine-photo" role="img" aria-label="Photo of a large office multifunction copier, model Q Module 738K, with finisher and paper trays"></div>

  <div class="feature-burst">
    <svg viewBox="-100 -100 200 200" aria-hidden="true">
      <polygon fill="var(--burst)" points="100,0 76,15 92,38 65,43 71,71 43,65 38,92 15,76 0,100 -15,76 -38,92 -43,65 -71,71 -65,43 -92,38 -76,15 -100,0 -76,-15 -92,-38 -65,-43 -71,-71 -43,-65 -38,-92 -15,-76 0,-100 15,-76 38,-92 43,-65 71,-71 65,-43 92,-38 76,-15"/>
    </svg>
    <p>ALL<br>COPIERS<br>CAN SCAN,<br>PRINT<br>&amp; FAX</p>
  </div>

  <p class="billing-note">...with 10,000 secure<br>customer codes which<br>count copies, prints,scans<br>and faxes for acurate<br>billing.</p>

  <h2 class="contract-line">No Lock-in Contracts</h2>

  <div class="brand-name">Brightvane<br>Printers</div>

  <p class="service-area">Available in Sydney<br>and Inner Suburbs</p>

  <footer class="contact-bar">1800 27 91 58<span class="divider">|</span>info@brightvaneprinters.com.au</footer>
</main>
</body>
</html>
```